Business Card / Appointment Card for Physician

On one side it should give the logo, address, and contact information, and on the other side it should br an Appointment card.

One Side:
Logo (see attached files)
Board Certified American Orthopedic Surgery

1874 Larkmoor Ave.
Suite KP7
Bronx, NY 10287
Tel: (718) 555 - 0142
Fax: (718) 555 - 0187

612 Ninth Ave.
Suite 42
New York, NY 10089
Tel: (212) 555 - 0163

Second Side:
Appointment
give them a choice of Bronx or Mahattan office
For:
Date:
Time:

If you are unable to keep your appointment, please call (718) 555-0129 24hrs in advance.

Target Market(s)

People that need orthopedic surgery

Industry/Entity Type

Business

Contact Information for Business Card

smart and attractive

Requirements
Must have
• logo
• contact information on one side, appointment information on the other

```html
<!DOCTYPE html>
<html lang="en">
<head>
<meta charset="utf-8">
<title>Appointment and Contact Card</title>
<link href="https://fonts.googleapis.com/css2?family=Open+Sans:wght@400;600;700&display=swap" rel="stylesheet">
<style>
  :root {
    --backdrop: #1c1c1e;
    --card: #ffffff;
    --navy-blue: #1570b8;
    --sky-blue: #29abe2;
    --leaf-green: #7ac143;
    --ink: #3a3a3a;
    --rule: #2a7fc0;
  }
  * { box-sizing: border-box; margin: 0; padding: 0; }
  html, body { width: 1200px; height: 1200px; overflow: hidden; }
  body {
    background: var(--backdrop);
    font-family: "Open Sans", sans-serif;
    color: var(--ink);
    position: relative;
  }
  .card {
    position: absolute;
    left: 160px;
    width: 880px;
    height: 503px;
    background: var(--card);
    overflow: hidden;
  }
  .appointment-card { top: 50px; }
  .contact-card { top: 620px; }

  /* Appointment side */
  .appointment-title {
    position: absolute; left: 0; width: 560px; top: 62px;
    text-align: center;
    font-weight: 700; font-size: 36px; letter-spacing: 1px;
    color: var(--navy-blue);
  }
  .office-name {
    position: absolute; left: 0; width: 560px; top: 112px;
    text-align: center;
    font-weight: 600; font-size: 20px;
    color: var(--sky-blue);
  }
  .field-label {
    position: absolute; font-size: 25px; color: var(--ink);
  }
  .field-line {
    position: absolute; height: 2px; background: var(--rule);
  }
  .meridiem {
    position: absolute; font-size: 20px; color: var(--ink);
  }
  .day-row {
    position: absolute; left: 70px; top: 330px;
    display: flex; gap: 40px;
  }
  .day {
    display: flex; align-items: center; gap: 10px;
    font-size: 25px;
  }
  .checkbox {
    width: 22px; height: 22px;
    border: 2.5px solid var(--navy-blue);
  }
  .cancellation-note {
    position: absolute; left: 0; width: 880px; top: 410px;
    text-align: center; font-size: 17px; line-height: 1.35;
  }

  /* Contact side */
  .practice-mark {
    position: absolute; right: 50px; top: 50px;
    display: flex; align-items: center; gap: 14px;
  }
  .practice-dot {
    width: 52px; height: 52px; border-radius: 50%;
    background: var(--navy-blue);
  }
  .practice-name {
    font-weight: 600; font-size: 24px; color: var(--navy-blue);
  }
  .office-address {
    position: absolute; left: 70px;
    font-size: 21px; line-height: 1.25; font-style: normal;
  }
  .office-address.bronx { top: 150px; }
  .office-address.manhattan { top: 305px; }
  .contact-label { color: var(--sky-blue); }
  .card-band {
    position: absolute; left: 0; bottom: 0; width: 880px; height: 80px;
  }
  .certification {
    position: absolute; right: 34px; bottom: 22px;
    font-size: 20px; color: #ffffff; white-space: nowrap;
  }
</style>
</head>
<body>

  <section class="card appointment-card" aria-label="Appointment side">
    <h1 class="appointment-title">APPOINTMENT</h1>
    <p class="office-name">Bronx office</p>

    <span class="field-label" style="left:70px; top:195px;">For :</span>
    <div class="field-line" style="left:150px; top:225px; width:670px;"></div>

    <span class="field-label" style="left:70px; top:260px;">Date :</span>
    <div class="field-line" style="left:160px; top:290px; width:260px;"></div>

    <span class="field-label" style="left:450px; top:260px;">Time :</span>
    <div class="field-line" style="left:540px; top:290px; width:200px;"></div>

    <span class="meridiem" style="left:752px; top:262px;">A.M.</span>
    <span class="meridiem" style="left:815px; top:262px;">P.M.</span>

    <div class="day-row">
      <div class="day"><span class="checkbox"></span>Mon.</div>
      <div class="day"><span class="checkbox"></span>Tues.</div>
      <div class="day"><span class="checkbox"></span>Wed.</div>
      <div class="day"><span class="checkbox"></span>Thurs.</div>
      <div class="day"><span class="checkbox"></span>Fri.</div>
      <div class="day"><span class="checkbox"></span>Sat.</div>
    </div>

    <p class="cancellation-note">If you are unable to keep your appointment, please call (718) 555-0129<br>24hrs in advance.</p>
  </section>

  <section class="card contact-card" aria-label="Contact side">
    <div class="practice-mark">
      <span class="practice-dot"></span>
      <span class="practice-name">DANIEL R. KESSLER MD PC</span>
    </div>

    <address class="office-address bronx">
      1874 Larkmoor Ave.<br>
      Suite KP7<br>
      Bronx, NY 10287<br>
      <span class="contact-label">Tel:</span> (718) 555 - 0142<br>
      <span class="contact-label">Fax:</span> (718) 555 - 0187
    </address>

    <address class="office-address manhattan">
      612 Ninth Ave.<br>
      Suite 42<br>
      New York, NY 10089<br>
      <span class="contact-label">Tel:</span> (212) 555 - 0163
    </address>

    <svg class="card-band" viewBox="0 0 880 80" aria-hidden="true">
      <polygon points="0,56 345,26 325,80 0,80" fill="var(--navy-blue)"/>
      <polygon points="360,0 378,0 358,80 340,80" fill="var(--leaf-green)"/>
      <polygon points="382,0 880,0 880,80 362,80" fill="var(--sky-blue)"/>
    </svg>
    <p class="certification">Board Certified American Orthopedic Surgery</p>
  </section>

</body>
</html>
```